Bodywork Quietude Business Card Design

I want to create a very elegant and sophisticated two sided business card for my massage practice (www.bodyworkquietude.net). I have attached the logo and a PDF with some ideas down for the back of the card but I am open to suggestions. I will want to tie in a post card and flyer to the card later.
Similar colors to website would be great.
Target Market(s)
High end clientele, people looking for a sophisticated spa experience.
Industry/Entity Type
Massage
Contact Information for Business Card
Bodywork Quietude
7318 Larkspur Ave S, Suite 305
Seattle, WA 98118
(206) 555-0147
www.bodyworkquietude.net
Look and feel

```html
<!DOCTYPE html>
<html lang="en">
<head>
<meta charset="utf-8">
<title>Bodywork Quietude – Business Card</title>
<link rel="stylesheet" href="https://fonts.googleapis.com/css2?family=Cormorant+Garamond:ital,wght@0,500;1,500&family=Roboto+Condensed:wght@300;400;700&display=swap">
<style>
  :root {
    --page: #e9e6e1;
    --card-white: #fbfbfa;
    --teal-dark: #1c3845;
    --teal-ink: #1f3d4b;
    --grey-text: #6f7478;
    --rule: #3e5360;
    --cream: #f3f1ec;
  }
  * { margin: 0; padding: 0; box-sizing: border-box; }
  html, body { width: 1200px; height: 911px; overflow: hidden; background: var(--page); }
  .canvas { position: relative; width: 1200px; height: 911px; }

  .card { position: absolute; border-radius: 22px; overflow: hidden; box-shadow: 0 10px 26px rgba(0,0,0,.18); }

  /* Front */
  .card-front { left: 52px; top: 123px; width: 380px; height: 665px; background: var(--card-white); }
  .front-brand {
    position: absolute; left: 0; right: 0; top: 150px;
    display: flex; align-items: center; justify-content: center; gap: 10px;
    font-family: "Cormorant Garamond", serif; font-weight: 500;
    font-size: 24px; letter-spacing: .04em; color: var(--teal-ink); text-transform: uppercase;
  }
  .brand-dot { width: 12px; height: 12px; border-radius: 50%; background: var(--teal-ink); flex: none; }
  .contact-band {
    position: absolute; left: 0; right: 0; top: 262px; height: 150px;
    border-top: 1.5px solid var(--rule); border-bottom: 1.5px solid var(--rule);
    padding: 22px 0 0 40px;
    font-family: "Roboto Condensed", sans-serif; color: var(--teal-ink);
  }
  .person { font-size: 21px; font-weight: 700; text-transform: uppercase; }
  .person .role { font-weight: 300; color: var(--grey-text); }
  .contact-line { font-size: 15px; font-weight: 300; color: #3c4a52; margin-top: 10px; }
  .contact-line b { font-weight: 700; color: var(--teal-ink); }

  /* Back */
  .card-back { left: 483px; top: 265px; width: 665px; height: 380px; background: var(--teal-dark); color: var(--cream); text-align: center; }
  .invitation {
    margin-top: 42px;
    font-family: "Cormorant Garamond", serif; font-style: italic; font-weight: 500;
    font-size: 26px; line-height: 1.22;
  }
  .back-brand {
    margin-top: 34px;
    font-family: "Cormorant Garamond", serif; font-weight: 500;
    font-size: 38px; letter-spacing: .05em; text-transform: uppercase;
  }
  .service {
    position: absolute; left: 0; right: 0; bottom: 44px;
    font-family: "Cormorant Garamond", serif; font-style: italic; font-weight: 500;
    font-size: 24px;
  }
</style>
</head>
<body>
<main class="canvas">
  <section class="card card-front" aria-label="Business card front">
    <div class="front-brand"><span class="brand-dot"></span>Bodywork Quietude</div>
    <div class="contact-band">
      <p class="person">Daniel Harper <span class="role">| CEO/Founder</span></p>
      <p class="contact-line"><b>P:</b> (206) 555-0147</p>
      <p class="contact-line"><b>W:</b> www.bodyworkquietude.net</p>
      <p class="contact-line">7318 Larkspur Ave S, Suite 305, Seattle, WA 98118</p>
    </div>
  </section>

  <section class="card card-back" aria-label="Business card back">
    <p class="invitation">Settle In and Discover the Most<br>Restful and Deeply Soothing<br>Hour of Your Week.....</p>
    <p class="back-brand">Bodywork Quietude</p>
    <p class="service">Slow Flow Restorative Bodywork</p>
  </section>
</main>
</body>
</html>
```